Oven Cleaning Business owner needs business card design

Hi there,
Would like for a business card to be designed for myself, the owner of a professional oven cleaning business on the Sunshine Coast.
Would like it to look sleek, and modern-ish. Bit creative is encouraged too.
Include following:
Name/title: Corin ter Haghe, Owner
Phone number: 1300 482 916
Email: info@hearthshinecrew.com.au
Website: www.hearthshinecrew.com.au

```html
<!DOCTYPE html>
<html lang="en">
<head>
<meta charset="utf-8">
<title>Hearthshine Crew – Business Card</title>
<link rel="stylesheet" href="https://fonts.googleapis.com/css2?family=Montserrat:wght@300;400;700&display=swap">
<style>
  :root {
    --stage: #1b1b1c;
    --card: #3d3d3e;
    --teal: #4fc4cd;
    --white: #ffffff;
    --ink: #111111;
  }
  * { box-sizing: border-box; margin: 0; padding: 0; }
  html, body {
    width: 1200px; height: 900px; overflow: hidden;
    background: var(--stage);
    font-family: "Montserrat", sans-serif;
  }
  .stage {
    position: relative; width: 1200px; height: 900px;
    display: flex; flex-direction: column; align-items: center; justify-content: center; gap: 44px;
  }
  .card {
    position: relative; width: 640px; height: 366px;
    background: var(--card); border-radius: 26px; overflow: hidden;
  }

  /* Back side */
  .card--back {
    display: flex; flex-direction: column; align-items: center; justify-content: center; gap: 22px;
  }
  .brand-dot {
    width: 96px; height: 96px; border-radius: 50%; background: var(--teal);
  }
  .brand-name {
    font-weight: 700; font-size: 38px; letter-spacing: 4px; text-transform: uppercase;
    color: var(--teal);
  }

  /* Front side */
  .card--front .brand-name {
    position: absolute; left: 40px; top: 40px;
    font-size: 28px; letter-spacing: 3px; color: var(--white);
  }
  .contact-list {
    position: absolute; left: 40px; bottom: 46px; list-style: none;
    display: flex; flex-direction: column; gap: 9px;
  }
  .contact-item {
    display: flex; align-items: center; gap: 12px;
    color: var(--white); font-size: 15px; font-weight: 400;
  }
  .contact-icon { width: 16px; height: 16px; flex: none; }
  .person {
    position: absolute; right: 62px; top: 150px; text-align: right;
  }
  .person-name {
    color: var(--teal); font-weight: 700; font-size: 21px; text-transform: uppercase; letter-spacing: 0.3px;
  }
  .person-title {
    color: var(--white); font-weight: 300; font-size: 17px; margin-top: 4px;
  }
  .accent-bar {
    position: absolute; right: 0; top: 150px; width: 30px; height: 54px; background: var(--teal);
  }
  .corner-dot {
    position: absolute; right: 120px; bottom: -60px;
    width: 190px; height: 190px; border-radius: 50%; background: var(--teal);
  }
</style>
</head>
<body>
<main class="stage">

  <section class="card card--back" aria-label="Card back">
    <div class="brand-dot" aria-hidden="true"></div>
    <p class="brand-name">Hearthshine Crew</p>
  </section>

  <section class="card card--front" aria-label="Card front">
    <p class="brand-name">Hearthshine Crew</p>

    <div class="person">
      <p class="person-name">Corin ter Haghe</p>
      <p class="person-title">Owner</p>
    </div>
    <div class="accent-bar" aria-hidden="true"></div>

    <ul class="contact-list">
      <li class="contact-item">
        <svg class="contact-icon" viewBox="0 0 16 16" aria-hidden="true">
          <path fill="#fff" d="M3.6 1.2l2.3 2.4-1.3 1.8c.9 1.9 2.2 3.2 4 4l1.8-1.3 2.4 2.3-1.3 2.6C6.8 12.8 2.9 8.9 1 4.2z"/>
        </svg>
        1300 482 916
      </li>
      <li class="contact-item">
        <svg class="contact-icon" viewBox="0 0 16 16" aria-hidden="true">
          <rect x="1" y="3" width="14" height="10" fill="#fff"/>
          <path d="M1 3l7 6 7-6" fill="none" stroke="#3d3d3e" stroke-width="1.3"/>
        </svg>
        info@hearthshinecrew.com.au
      </li>
      <li class="contact-item">
        <svg class="contact-icon" viewBox="0 0 16 16" aria-hidden="true">
          <circle cx="8" cy="8" r="6.5" fill="none" stroke="#fff" stroke-width="1.4"/>
          <ellipse cx="8" cy="8" rx="2.8" ry="6.5" fill="none" stroke="#fff" stroke-width="1.1"/>
          <path d="M1.5 8h13" stroke="#fff" stroke-width="1.1"/>
        </svg>
        www.hearthshinecrew.com.au
      </li>
    </ul>

    <div class="corner-dot" aria-hidden="true"></div>
  </section>

</main>
</body>
</html>
```